Velora Aesthetica

Medical doctor providing aesthetic medicine

* Double sided card
* Logo to be on card
Other details:
* Dr. Mirela Kostvan, BSc, MBChB, CCFP
* #214-215, 27903 83 Ave, Surrey, BC, V2T 4K7
* 604-718-2943
* info@veloraclinic.ca
* www.veloraclinic.ca

Industry/Entity Type

Medical / Health & Beauty

Contact Information for Business Card

see 'Project Description'

Colors
0054AA
0677BA
7BADD7
CADEEF
E8F1F8
FFF300
FFF600
FEFA6F
FFFEC7
FFFEE8

Requirements
Must have
• Modern, high-end design

```html
<!DOCTYPE html>
<html lang="en">
<head>
<meta charset="utf-8">
<title>Velora Aesthetica — Business Card</title>
<link rel="stylesheet" href="https://fonts.googleapis.com/css2?family=Poppins:wght@400;500;600&family=Montserrat:wght@500;600&display=swap">
<style>
  :root {
    --backdrop: #808080;
    --card-white: #ffffff;
    --navy: #22405f;
    --gold: #d6ae22;
    --ink: #1c1c1c;
    --divider: #b8b8b8;
  }
  * { box-sizing: border-box; margin: 0; padding: 0; }
  html, body {
    width: 1093px;
    height: 1200px;
    overflow: hidden;
    background: var(--backdrop);
  }
  .canvas {
    position: relative;
    width: 1093px;
    height: 1200px;
  }
  .card {
    position: absolute;
    left: 265px;
    width: 578px;
    height: 356px;
    border-radius: 26px;
    overflow: hidden;
  }
  .card--front { top: 227px; background: var(--card-white); }
  .card--back  { top: 621px; background: var(--navy); }

  .brand {
    position: absolute;
    display: flex;
    align-items: center;
    justify-content: center;
    font-family: "Montserrat", sans-serif;
    font-weight: 600;
    text-transform: uppercase;
    white-space: nowrap;
  }
  .brand__dot {
    flex: none;
    border-radius: 50%;
    background: var(--gold);
  }
  .card--front .brand {
    left: 20px;
    top: 150px;
    width: 260px;
    gap: 10px;
    font-size: 17px;
    letter-spacing: 2px;
    color: var(--ink);
  }
  .card--front .brand__dot { width: 14px; height: 14px; }

  .card--back .brand {
    left: 0;
    top: 154px;
    width: 100%;
    gap: 16px;
    font-size: 30px;
    letter-spacing: 5px;
    color: var(--card-white);
  }
  .card--back .brand__dot { width: 24px; height: 24px; }

  .divider {
    position: absolute;
    left: 288px;
    top: 73px;
    width: 1px;
    height: 209px;
    background: var(--divider);
  }
  .details {
    position: absolute;
    left: 312px;
    top: 88px;
    font-family: "Poppins", sans-serif;
    color: var(--ink);
  }
  .details__name {
    font-family: "Montserrat", sans-serif;
    font-weight: 600;
    font-size: 16px;
    letter-spacing: -0.3px;
    text-transform: uppercase;
    line-height: 21px;
  }
  .details__creds {
    font-weight: 600;
    font-size: 15px;
    color: var(--gold);
    line-height: 21px;
  }
  .contact {
    list-style: none;
    margin-top: 15px;
  }
  .contact__item {
    display: flex;
    align-items: center;
    gap: 7px;
    font-size: 16.5px;
    line-height: 21px;
  }
  .contact__icon { width: 15px; height: 15px; flex: none; fill: var(--gold); }
  .accent { color: var(--gold); }
  .address {
    margin-top: 17px;
    font-style: normal;
    font-size: 16.5px;
    line-height: 21px;
  }
</style>
</head>
<body>
<main class="canvas">

  <section class="card card--front" aria-label="Card front">
    <div class="brand"><span class="brand__dot"></span>Velora Aesthetica</div>
    <div class="divider"></div>
    <div class="details">
      <h1 class="details__name">Dr. Mirela Kostvan</h1>
      <p class="details__creds">BSc, MBChB, CCFP</p>
      <ul class="contact">
        <li class="contact__item">
          <svg class="contact__icon" viewBox="0 0 24 24" aria-hidden="true"><path d="M6.6 10.8a15.1 15.1 0 0 0 6.6 6.6l2.2-2.2c.3-.3.7-.4 1-.2 1.1.4 2.3.6 3.6.6.6 0 1 .4 1 1V20c0 .6-.4 1-1 1A17 17 0 0 1 3 4c0-.6.4-1 1-1h3.5c.6 0 1 .4 1 1 0 1.3.2 2.5.6 3.6.1.3 0 .7-.2 1z"/></svg>
          <span>604-718-2943</span>
        </li>
        <li class="contact__item">
          <svg class="contact__icon" viewBox="0 0 24 24" aria-hidden="true"><path d="M2 5h20v14H2z M2 5l10 8 10-8" stroke="#fff" stroke-width="1.4"/></svg>
          <span>info@veloraclinic.ca</span>
        </li>
        <li class="contact__item">
          <svg class="contact__icon" viewBox="0 0 24 24" aria-hidden="true"><circle cx="12" cy="12" r="10"/><path d="M2 12h20M12 2v20M12 2c-3 3-4 6.5-4 10s1 7 4 10M12 2c3 3 4 6.5 4 10s-1 7-4 10M4 7h16M4 17h16" stroke="#fff" stroke-width="1.1" fill="none"/></svg>
          <span>www.<span class="accent">veloraclinic</span>.ca</span>
        </li>
      </ul>
      <address class="address">#214-215, 27903 83 Ave,<br>Surrey, BC, V2T 4K7</address>
    </div>
  </section>

  <section class="card card--back" aria-label="Card back">
    <div class="brand"><span class="brand__dot"></span>Velora Aesthetica</div>
  </section>

</main>
</body>
</html>
```